NEW Modern Sleek Business Card for VR Language Startup

Our startup is using VR to lead the next wave of world language education. We need a two-sided business card that introduces the larger organization (Quorvel Language Inc) and our contact info on one side and shows the product, Lumidrasca, on the other side.

Side 1 (contact info)= Quorvel Logo and Contact info (name, title, phone, email)

Side 2 (product)= Lumidrasc logo, text, and website
Text= Culturally Immersive Language Learning Games
Website= www.lumidrasc.example

Target Market(s)

Education, Technology

Contact Information for Business Card

Contact info will be updated upon approval of the design. For now, put this as a placeholder.

Perry Hollins
Founder & CEO
phollins@mailtrove.example
(555)-014-2736

Font styles to use
Other font styles liked:
• Gibson and Century Gothic are the brand fonts

Requirements
Nice to have
• I would love to see cohesion between the design and colors of the two logos. I have attached a few business card designs that I like, so you can get a feel for my preferred style.

```html
<!DOCTYPE html>
<html lang="en">
<head>
<meta charset="utf-8">
<title>Lumidrasc &amp; Quorvel Language – Business Card</title>
<link rel="stylesheet" href="https://fonts.googleapis.com/css2?family=Montserrat:wght@600;700&family=Questrial&display=swap">
<style>
  :root {
    --backdrop: #18181b;
    --card: #232527;
    --card-edge: #2c2f31;
    --ink: #f4f5f7;
    --ink-soft: #d9dce0;
    --accent-cyan: #3cc3ee;
    --accent-violet: #7a5fd6;
    --accent-coral: #f24e6a;
    --accent-orange: #f7873a;
  }
  * { margin: 0; padding: 0; box-sizing: border-box; }
  html, body {
    width: 1200px; height: 800px; overflow: hidden;
    background: var(--backdrop);
  }
  .canvas {
    position: relative; width: 1200px; height: 800px;
    display: flex; justify-content: center; align-items: center; gap: 80px;
  }
  .card {
    position: relative; width: 360px; height: 630px;
    background: var(--card);
    border: 1px solid var(--card-edge);
    color: var(--ink);
    font-family: "Questrial", "Century Gothic", sans-serif;
    overflow: hidden;
  }

  /* Product side */
  .product-brand {
    position: absolute; top: 110px; left: 0; right: 0;
    display: flex; flex-direction: column; align-items: center; gap: 22px;
  }
  .brand-dot {
    width: 110px; height: 110px; border-radius: 50%;
    background: var(--accent-cyan);
  }
  .product-name {
    font-family: "Montserrat", "Century Gothic", sans-serif;
    font-weight: 700; font-size: 40px; letter-spacing: 0.5px;
    color: var(--ink);
  }
  .product-tagline {
    position: absolute; top: 350px; left: 0; right: 0;
    text-align: center; text-transform: uppercase;
    font-size: 19px; line-height: 1.55; letter-spacing: 2.5px;
    color: var(--ink);
  }
  .product-website {
    position: absolute; bottom: 70px; left: 0; right: 0;
    text-align: center; font-size: 19px; letter-spacing: 1px;
    color: var(--ink);
  }

  /* Contact side */
  .company-brand {
    position: absolute; top: 110px; left: 0; right: 0;
    display: flex; flex-direction: column; align-items: center; gap: 22px;
  }
  .company-dot {
    width: 110px; height: 110px; border-radius: 50%;
    background: var(--accent-coral);
  }
  .company-name {
    font-family: "Montserrat", "Century Gothic", sans-serif;
    font-weight: 700; font-size: 34px; letter-spacing: 6px;
    line-height: 1.2; text-align: center; text-transform: uppercase;
    color: var(--ink);
  }
  .contact {
    position: absolute; left: 38px; right: 24px; bottom: 70px;
  }
  .contact-name {
    font-family: "Montserrat", "Century Gothic", sans-serif;
    font-weight: 700; font-size: 21px; letter-spacing: 1.5px;
    text-transform: uppercase;
  }
  .contact-title {
    font-size: 17px; color: var(--ink-soft); margin-top: 4px; margin-bottom: 22px;
  }
  .contact-line {
    display: flex; align-items: center; gap: 10px;
    font-size: 15px; color: var(--ink-soft); margin-top: 8px;
  }
  .contact-icon { width: 22px; height: 22px; flex: none; }
</style>
</head>
<body>
  <main class="canvas">

    <section class="card card-product" aria-label="Product side">
      <div class="product-brand">
        <div class="brand-dot"></div>
        <div class="product-name">Lumidrasc</div>
      </div>
      <p class="product-tagline">Culturally Immersive<br>Language<br>Learning Games</p>
      <p class="product-website">www.lumidrasc.example</p>
    </section>

    <section class="card card-contact" aria-label="Contact side">
      <div class="company-brand">
        <div class="company-dot"></div>
        <div class="company-name">Quorvel<br>Language</div>
      </div>
      <div class="contact">
        <div class="contact-name">Perry Hollins</div>
        <div class="contact-title">Founder &amp; CEO</div>
        <div class="contact-line">
          <svg class="contact-icon" viewBox="0 0 22 22" aria-hidden="true">
            <circle cx="11" cy="11" r="11" fill="var(--accent-orange)"/>
            <path d="M7.5 6.2c.5-.4 1.2-.3 1.5.2l1 1.6c.3.5.2 1.1-.3 1.4l-.6.4c.5 1.2 1.4 2.1 2.6 2.6l.4-.6c.3-.5.9-.6 1.4-.3l1.6 1c.5.3.6 1 .2 1.5l-.6.7c-.6.7-1.6.9-2.5.5-2.3-1-4.1-2.8-5.1-5.1-.4-.9-.2-1.9.5-2.5z" fill="#fff"/>
          </svg>
          <span>(555)-014-2736</span>
        </div>
        <div class="contact-line">
          <svg class="contact-icon" viewBox="0 0 22 22" aria-hidden="true">
            <circle cx="11" cy="11" r="11" fill="var(--accent-violet)"/>
            <rect x="5.5" y="7" width="11" height="8" rx="1" fill="none" stroke="#fff" stroke-width="1.4"/>
            <path d="M5.8 7.4 11 11.6l5.2-4.2" fill="none" stroke="#fff" stroke-width="1.4"/>
          </svg>
          <span>phollins@mailtrove.example</span>
        </div>
      </div>
    </section>

  </main>
</body>
</html>
```